Business Card Design

Carl Benson Insurance Agency, an Independent Insurance Agency which was stated on Orchard Lane in Laplace, Louisiana on 1958 and has grown the six locations throughout South Louisiana. We sell personal (auto Homeowners flood, liability) and commercial insurance (commercial property, general liability, workers compensation, commercial auto). I am looking for a double sided card with list the five remaining locations on the back or maybe even a folded four sided card. Our home office is a two story building with a green roof. I have had a logo designed which I have attached. Open for revisions but would like to stay with in the same green roof over an M. I have attached the logo but can not tell if I was uploaded.

Target Market(s)

Individual and commercial insurance buyers. Upper income and business owners

Industry/Entity Type

Insurance

Requirements
Must have
• Must have similar logo as uploaded. Green roof over M or something similar. List all location address and phone numbers.

Employee name, office phone number; direct phone line; email address and website list all locations on card. Very Similar colors to current logo.
Nice to have
• Possible folded card with double sided print

```html
<!DOCTYPE html>
<html lang="en">
<head>
<meta charset="utf-8">
<title>Carl Benson Insurance Agency – Business Card</title>
<link rel="stylesheet" href="https://fonts.googleapis.com/css2?family=Open+Sans:wght@400;600;700;800&display=swap">
<style>
  :root {
    --page-bg: #e9e7e3;
    --card-bg: #ffffff;
    --green: #1f5b45;
    --blue: #2a6fb0;
    --blue-light: #3a8fd0;
    --grey: #7a7f82;
    --ink: #222426;
  }
  * { box-sizing: border-box; margin: 0; padding: 0; }
  html, body {
    width: 1200px; height: 1023px; overflow: hidden;
    background: var(--page-bg);
    font-family: "Open Sans", Arial, sans-serif;
    color: var(--ink);
  }
  .card {
    position: absolute; left: 220px;
    width: 760px; height: 434px;
    background: var(--card-bg);
    box-shadow: 0 6px 18px rgba(0,0,0,.18);
    overflow: hidden;
  }
  .card--front { top: 56px; }
  .card--back  { top: 533px; }

  /* front */
  .brand {
    position: absolute; right: 44px; top: 46px;
    display: flex; align-items: center; gap: 14px;
  }
  .brand__mark { width: 44px; height: 44px; background: var(--green); }
  .brand__name {
    font-weight: 800; font-size: 27px; line-height: 1.05;
    color: var(--green); text-transform: uppercase;
  }
  .brand__tagline {
    font-weight: 600; font-size: 15px; color: var(--grey); margin-top: 4px;
  }
  .divider {
    position: absolute; left: 40px; right: 40px; top: 222px;
    height: 2px; background: var(--green);
  }
  .person { position: absolute; left: 44px; top: 158px; }
  .person__name { font-weight: 700; font-size: 28px; color: var(--green); }
  .person__role { font-size: 18px; color: var(--green); }
  .contacts {
    position: absolute; left: 44px; top: 244px;
    list-style: none; font-size: 17px; line-height: 27px;
  }
  .contacts li { display: flex; align-items: center; gap: 12px; }
  .contacts svg { width: 16px; height: 16px; flex: none; }
  .address {
    position: absolute; right: 44px; top: 250px;
    text-align: right; font-size: 17px; line-height: 26px;
  }
  .band {
    position: absolute; left: 0; right: 0; bottom: 0; height: 34px;
    display: flex;
  }
  .band__blue { flex: 1; background: linear-gradient(var(--blue-light), var(--blue)); }
  .band__green { width: 110px; background: var(--green); }

  /* back */
  .back-brand {
    position: absolute; left: 70px; top: 70px;
    display: flex; align-items: center; gap: 20px;
  }
  .back-brand__mark { width: 70px; height: 70px; background: var(--green); }
  .back-brand__name {
    font-weight: 800; font-size: 50px; line-height: 1.02;
    color: var(--green); text-transform: uppercase;
  }
  .back-info { position: absolute; left: 70px; top: 232px; }
  .back-info__tagline { font-weight: 600; font-size: 34px; color: var(--grey); }
  .back-info__visit { font-size: 22px; color: var(--blue); margin-top: 4px; }
  .locations {
    list-style: none; display: flex; gap: 10px; margin-top: 16px;
    font-weight: 700; font-size: 17px; letter-spacing: 1.5px; color: var(--green);
  }
  .locations li + li::before { content: "•"; margin-right: 10px; }
</style>
</head>
<body>

<section class="card card--front">
  <div class="brand">
    <div class="brand__mark"></div>
    <div>
      <div class="brand__name">Carl Benson<br>Insurance Agency</div>
      <div class="brand__tagline">Serving Orchard Lane Since 1958</div>
    </div>
  </div>

  <div class="person">
    <div class="person__name">Maren Doyle</div>
    <div class="person__role">Manager</div>
  </div>
  <div class="divider"></div>

  <ul class="contacts">
    <li>
      <svg viewBox="0 0 16 16"><path d="M3 2h3l1 4-2 1a8 8 0 0 0 4 4l1-2 4 1v3a2 2 0 0 1-2 2A12 12 0 0 1 1 4a2 2 0 0 1 2-2z" fill="#555"/></svg>
      555-204-7100
    </li>
    <li>
      <svg viewBox="0 0 16 16"><rect x="4" y="1" width="8" height="14" rx="1.5" fill="none" stroke="#555" stroke-width="1.5"/></svg>
      5550137482
    </li>
    <li>
      <svg viewBox="0 0 16 16"><rect x="1" y="3" width="14" height="10" fill="none" stroke="#555" stroke-width="1.5"/><path d="M1 3l7 6 7-6" fill="none" stroke="#555" stroke-width="1.5"/></svg>
      maya.ross@carlbenson.com
    </li>
    <li>
      <svg viewBox="0 0 16 16"><rect x="1" y="2" width="14" height="10" fill="none" stroke="#555" stroke-width="1.5"/><path d="M5 15h6M8 12v3" stroke="#555" stroke-width="1.5"/></svg>
      www.carlbensoninsurance.com
    </li>
  </ul>

  <address class="address" style="font-style:normal">
    2240 Riverbend Pkwy, Suite B<br>
    Cedar Falls LA 70099
  </address>

  <div class="band"><div class="band__blue"></div><div class="band__green"></div></div>
</section>

<section class="card card--back">
  <div class="back-brand">
    <div class="back-brand__mark"></div>
    <div class="back-brand__name">Carl Benson<br>Insurance Agency</div>
  </div>
  <div class="back-info">
    <div class="back-info__tagline">Serving Orchard Lane Since 1958</div>
    <div class="back-info__visit">Visit one of our 6 convenient locations</div>
    <ul class="locations">
      <li>Ashford</li>
      <li>Belmont</li>
      <li>Crestview</li>
      <li>Dunmore</li>
      <li>Elmwood</li>
    </ul>
  </div>
</section>

</body>
</html>
```